Business Card for Amber Heron Advisors

Business card design for Amber Heron Advisors, a new consulting and financial advisory firm. I would like the designs to integrate the logo attached (at least on 1 side).

Target Market(s)

individual and institutional clients

Contact Information for Business Card

Dominic L. Hartwell, CFA
Managing Director
amberheronadvisors.examplep
hartwell@amberheronadvisors.example
(555) 218-4903

```html
<!DOCTYPE html>
<html lang="en">
<head>
<meta charset="utf-8">
<title>Amber Heron Advisors – Business Card</title>
<link rel="stylesheet" href="https://fonts.googleapis.com/css2?family=Lato:wght@400;700&display=swap">
<style>
  :root {
    --page-bg: #ececec;
    --card-bg: #141414;
    --card-bg-edge: #0c0c0c;
    --accent: #e3832a;
    --text-light: #ffffff;
    --divider: #8a8a8a;
  }
  * { margin: 0; padding: 0; box-sizing: border-box; }
  html, body {
    width: 1200px;
    height: 586px;
    overflow: hidden;
    background: var(--page-bg);
    font-family: "Lato", Arial, sans-serif;
  }
  .canvas {
    position: relative;
    width: 1200px;
    height: 586px;
  }
  .card {
    position: absolute;
    top: 128px;
    width: 502px;
    height: 302px;
    background: radial-gradient(ellipse at 50% 40%, var(--card-bg) 0%, var(--card-bg-edge) 100%);
  }
  .card--front { left: 65px; }
  .card--back  { left: 608px; }

  .brand-name {
    position: absolute;
    transform: translateX(-50%);
    text-align: center;
    color: var(--accent);
    font-weight: 700;
    text-transform: uppercase;
    line-height: 1;
    white-space: nowrap;
  }
  .brand-name__main { display: block; font-size: 34px; letter-spacing: 1px; }
  .brand-name__sub  { display: block; font-size: 13px; letter-spacing: 5px; margin-top: 8px; }
  .card--front .brand-name { left: 251px; top: 126px; }
  .card--back  .brand-name { left: 251px; top: 58px; }

  .person {
    position: absolute;
    right: 279px;
    top: 196px;
    text-align: right;
    white-space: nowrap;
  }
  .person__name {
    color: var(--accent);
    font-weight: 700;
    font-size: 16px;
  }
  .person__title {
    color: var(--text-light);
    font-size: 12px;
    margin-top: 5px;
  }

  .divider {
    position: absolute;
    left: 245px;
    top: 164px;
    width: 2px;
    height: 120px;
    background: linear-gradient(to bottom, transparent, var(--divider) 30%, var(--divider) 70%, transparent);
  }

  .contact {
    position: absolute;
    left: 271px;
    top: 186px;
    list-style: none;
    white-space: nowrap;
  }
  .contact__item {
    display: flex;
    align-items: center;
    height: 16px;
    margin-bottom: 9px;
    color: var(--text-light);
    font-weight: 700;
    font-size: 11px;
  }
  .contact__icon { width: 13px; height: 11px; margin-right: 8px; flex: none; }
  .contact__item--web { color: var(--accent); font-size: 12px; }
</style>
</head>
<body>
<main class="canvas">
  <section class="card card--front" aria-label="Card front">
    <div class="brand-name">
      <span class="brand-name__main">Amber Heron</span>
      <span class="brand-name__sub">Advisors</span>
    </div>
  </section>

  <section class="card card--back" aria-label="Card back">
    <div class="brand-name">
      <span class="brand-name__main">Amber Heron</span>
      <span class="brand-name__sub">Advisors</span>
    </div>

    <div class="person">
      <p class="person__name">Dominic L. Hartwell, CFA</p>
      <p class="person__title">Managing Director</p>
    </div>

    <div class="divider"></div>

    <ul class="contact">
      <li class="contact__item">
        <svg class="contact__icon" viewBox="0 0 13 11" aria-hidden="true">
          <path d="M1 4 Q6.5 0 12 4 L10.5 5 L9 3.6 L4 3.6 L2.5 5 Z" fill="#e3832a"/>
          <rect x="2.5" y="5" width="8" height="5.5" rx="1" fill="#e3832a"/>
          <circle cx="6.5" cy="7.7" r="1.4" fill="#141414"/>
        </svg>
        (555) 218-4903
      </li>
      <li class="contact__item">
        <svg class="contact__icon" viewBox="0 0 13 11" aria-hidden="true">
          <rect x="0.5" y="1" width="12" height="9" fill="#e3832a"/>
          <path d="M0.5 1 L6.5 6 L12.5 1" fill="none" stroke="#141414" stroke-width="1.2"/>
        </svg>
        hartwell@amberheronadvisors.example
      </li>
      <li class="contact__item contact__item--web">www.amberheronadvisors.examplep</li>
    </ul>
  </section>
</main>
</body>
</html>
```